Virtual Reality immersive experiences

Print ad 8.5" X 11"
Advertising to have people come rent time in our virtual reality room.
Fun for all ages
Unique experience
Immersive experience into 3D world
Escape reality
Be at heart of action - bottom of the ocean, travel the world, fight the invaders, solve the mystery and so much more
System used is Brelvo Optra
Dedicated room
Family friendly
$24 half hour
$40 per hour
Updates

Industry/Entity Type

Advertising

Requirements
Must have
• Be fun looking
• Eye catching
• Great pictures of VR experiences
• Pricing is $24 / 30 minutes and $40 / 1 hour
• Our location: 587 Larch Avenue, Three Hills, Alberta
• Our contact: 403-618-2093
• I have attached TERMALDO Technology Solutions logo which should be somewhere on the ad.
Nice to have
• could use phrases like: travel the world, explore the ocean depths, fight the invaders, visit the carnival

```html
<!DOCTYPE html>
<html lang="en">
<head>
<meta charset="utf-8">
<title>TERMALDO Technology Solutions – VR Room Flyer</title>
<link rel="stylesheet" href="https://fonts.googleapis.com/css2?family=Bowlby+One&family=Oswald:wght@500&display=swap">
<style>
  :root {
    --page: #e8e8ea;
    --paper: #ffffff;
    --blue: #0e4fa2;
    --blue-deep: #0a3f86;
    --sky: #1d9ad8;
    --green: #6dbb45;
    --ink: #2a2a2e;
    --logo: #1a8fd0;
  }
  * { margin: 0; padding: 0; box-sizing: border-box; }
  html, body { width: 1200px; height: 990px; overflow: hidden; background: var(--page); }
  .flyer {
    position: absolute; left: 240px; top: 29px;
    width: 720px; height: 932px;
    background: var(--paper);
    overflow: hidden;
    box-shadow: 0 6px 24px rgba(0,0,0,.18);
    font-family: "Bowlby One", "Arial Black", sans-serif;
  }
  .flyer__shapes { position: absolute; inset: 0; width: 720px; height: 932px; }
  .brand {
    position: absolute; left: 36px; top: 148px;
    display: flex; align-items: center; gap: 10px;
    font-family: "Oswald", "Arial Narrow", sans-serif; font-weight: 500;
    color: var(--logo); text-transform: uppercase; line-height: 1;
  }
  .brand__dot { width: 14px; height: 14px; border-radius: 50%; background: var(--logo); }
  .brand__name { font-size: 32px; letter-spacing: 2px; }
  .brand__sub { font-size: 12px; letter-spacing: 1.6px; margin-top: 4px; }
  .headline {
    position: absolute; left: 40px; top: 272px;
    color: #fff; font-size: 24px; line-height: 36px; text-transform: uppercase;
  }
  .tagline {
    position: absolute; left: 40px; top: 408px;
    background: var(--green); color: #fff;
    font-size: 17px; padding: 7px 18px; text-transform: uppercase;
  }
  .system {
    position: absolute; left: 40px; top: 470px;
    color: #fff; font-size: 20px; line-height: 30px; text-transform: uppercase;
  }
  .price {
    position: absolute; width: 132px; height: 132px; border-radius: 50%;
    background: var(--green); border: 5px solid #fff;
    color: #fff; display: flex; flex-direction: column; align-items: center; justify-content: center;
    line-height: 1;
  }
  .price__amount { font-size: 44px; }
  .price__term { font-family: "Oswald", sans-serif; font-weight: 500; font-size: 14px; letter-spacing: 1px; margin-top: 4px; }
  .price--hour { left: 566px; top: 404px; }
  .price--half { left: 430px; top: 464px; }
  .gear-photo {
    position: absolute; left: 440px; top: 668px; width: 210px; height: 118px;
    border-radius: 26px;
    background: linear-gradient(160deg, #4a4a50 0%, #2a2a2f 60%, #1a1a1e 100%);
  }
  .contact { position: absolute; left: 40px; top: 822px; text-transform: uppercase; }
  .contact__lead { color: var(--blue); font-size: 26px; line-height: 30px; }
  .contact__sub { color: var(--ink); font-size: 15px; line-height: 20px; }
  .contact__phone { color: var(--ink); font-size: 34px; line-height: 42px; display: flex; align-items: center; gap: 8px; }
  .visit { position: absolute; right: 40px; top: 800px; text-align: right; text-transform: uppercase; }
  .visit__lead { color: var(--blue); font-size: 24px; line-height: 30px; display: flex; align-items: center; justify-content: flex-end; gap: 6px; }
  .visit__line { color: var(--ink); font-size: 18px; line-height: 24px; }
</style>
</head>
<body>
<main class="flyer">
  <svg class="flyer__shapes" viewBox="0 0 720 932">
    <defs>
      <linearGradient id="arena" x1="0" y1="0" x2="1" y2="1">
        <stop offset="0" stop-color="#2f8a2a"/><stop offset=".55" stop-color="#6cc23a"/><stop offset="1" stop-color="#b6df48"/>
      </linearGradient>
      <linearGradient id="space" x1="0" y1="0" x2="1" y2="1">
        <stop offset="0" stop-color="#8a9a52"/><stop offset=".45" stop-color="#4d6f6a"/><stop offset="1" stop-color="#12201c"/>
      </linearGradient>
      <linearGradient id="dance" x1="0" y1="0" x2="1" y2="1">
        <stop offset="0" stop-color="#2b5fd0"/><stop offset=".5" stop-color="#d23a46"/><stop offset="1" stop-color="#101c58"/>
      </linearGradient>
      <linearGradient id="ocean" x1="0" y1="0" x2="0" y2="1">
        <stop offset="0" stop-color="#4a9ae0"/><stop offset=".6" stop-color="#225c9c"/><stop offset="1" stop-color="#0c2c58"/>
      </linearGradient>
    </defs>
    <polygon role="img" aria-label="Photo of a player wearing a VR headset and holding controllers in a green virtual arena" points="330,0 720,0 720,205 236,262" fill="url(#arena)"/>
    <polygon points="0,232 430,196 0,320" fill="var(--sky)"/>
    <polygon points="0,270 720,198 720,560 0,668" fill="var(--blue)"/>
    <polygon points="560,220 720,205 720,330" fill="var(--blue-deep)"/>
    <polygon points="0,660 720,552 720,574 0,682" fill="var(--sky)"/>
    <polygon role="img" aria-label="Game scene of a spaceship battle in outer space" points="0,640 240,600 240,773 0,800" fill="url(#space)"/>
    <polygon role="img" aria-label="Silhouette of a player in a neon light burst game scene" points="240,600 480,560 480,747 240,773" fill="url(#dance)"/>
    <polygon role="img" aria-label="Underwater scene with a whale in the ocean depths" points="480,560 720,520 720,720 480,747" fill="url(#ocean)"/>
    <polygon points="0,800 720,720 720,732 0,812" fill="var(--sky)"/>
  </svg>

  <div class="gear-photo" role="img" aria-label="Product photo of a VR headset with two hand controllers"></div>

  <div class="brand">
    <span class="brand__dot"></span>
    <div>
      <div class="brand__name">TERMALDO</div>
      <div class="brand__sub">Technology Solutions</div>
    </div>
  </div>

  <h1 class="headline">Travel the world,<br>explore the ocean depths,<br>fight the invaders, visit the carnival</h1>
  <p class="tagline">Feel immersive experience into 3D world</p>
  <p class="system">System used is Brelvo Optra<br>with dedicated room</p>

  <div class="price price--hour"><span class="price__amount">$40</span><span class="price__term">/ 1 HOUR</span></div>
  <div class="price price--half"><span class="price__amount">$24</span><span class="price__term">/30 MINUTES</span></div>

  <section class="contact">
    <p class="contact__lead">Call us today</p>
    <p class="contact__sub">For more information</p>
    <p class="contact__phone">
      <svg width="26" height="26" viewBox="0 0 24 24" aria-hidden="true"><path fill="#2a2a2e" d="M6.6 10.8a15.1 15.1 0 0 0 6.6 6.6l2.2-2.2a1 1 0 0 1 1-.25 11.4 11.4 0 0 0 3.6.57 1 1 0 0 1 1 1V20a1 1 0 0 1-1 1A17 17 0 0 1 3 4a1 1 0 0 1 1-1h3.5a1 1 0 0 1 1 1c0 1.25.2 2.45.57 3.57a1 1 0 0 1-.25 1z"/></svg>
      403-618-2093
    </p>
  </section>

  <section class="visit">
    <p class="visit__lead">Visit us
      <svg width="16" height="20" viewBox="0 0 16 20" aria-hidden="true"><path fill="none" stroke="#2a2a2e" stroke-width="2" d="M8 19s6-6.5 6-11A6 6 0 0 0 2 8c0 4.5 6 11 6 11z"/><circle cx="8" cy="8" r="2" fill="#2a2a2e"/></svg>
    </p>
    <p class="visit__line">587 Larch Avenue</p>
    <p class="visit__line">Three Hills, Alberta</p>
  </section>
</main>
</body>
</html>
```